Urine collection cup with and without sterile seal sticker

Hello. We need a urine cup label designed please with

Name:
Date of Birth:
Date:
Time:
Temp℃:
Specimen ID:

Product code: TUB-47
Volume markings (e.g., 30 mL, 60 mL, 90 mL).
Vela Drug Tests logo

Could you please provide one version with the additional sterile sticker extending to the top, and one version without the additional sterile sticker?

```html
<!DOCTYPE html>
<html lang="en">
<head>
<meta charset="utf-8">
<title>Vela Drug Tests – Urine Cup Labels</title>
<link href="https://fonts.googleapis.com/css2?family=Montserrat:wght@500;600;800&display=swap" rel="stylesheet">
<style>
  :root {
    --bg: #d0d0d0;
    --navy: #0b1f38;
    --blue: #28a3e4;
    --ink: #0f1e35;
    --rule: #7d7d7d;
    --card: #ffffff;
    --mark: #f6f6f6;
  }
  * { box-sizing: border-box; margin: 0; padding: 0; }
  html, body { width: 1200px; height: 1200px; overflow: hidden; }
  body {
    background: var(--bg);
    font-family: "Montserrat", sans-serif;
    position: relative;
  }
  .label { position: absolute; }
  .label-card {
    position: absolute;
    background: var(--card);
    border-radius: 22px 0 0 22px;
    box-shadow: 4px 6px 10px rgba(0,0,0,0.18);
    overflow: hidden;
  }
  .card-mark {
    position: absolute;
    border-radius: 50%;
    background: var(--mark);
  }
  .field {
    position: absolute;
    left: 39px;
    width: 397px;
    display: flex;
    align-items: flex-end;
    font-size: 23px;
    line-height: 28px;
    font-weight: 500;
    color: var(--ink);
  }
  .field-rule {
    flex: 1;
    border-bottom: 1px solid var(--rule);
    margin: 0 0 5px 8px;
  }
  .brand-strip {
    position: absolute;
    width: 99px;
    background: var(--navy);
    border-radius: 0 37px 0 0;
    box-shadow: 5px 6px 10px rgba(0,0,0,0.2);
  }
  .brand-dot {
    position: absolute;
    width: 48px; height: 48px;
    border-radius: 50%;
    background: var(--blue);
    left: 50%;
    transform: translateX(-50%);
  }
  .brand-name {
    position: absolute;
    left: 50%;
    transform: translateX(-50%);
    writing-mode: vertical-rl;
    font-size: 24px;
    font-weight: 800;
    color: #ffffff;
    white-space: nowrap;
    letter-spacing: 0.2px;
  }
  .code-band {
    position: absolute;
    inset: 0;
    background: var(--blue);
    clip-path: polygon(0 322px, 100% 302px, 100% 100%, 0 100%);
  }
  .product-code {
    position: absolute;
    left: 50%;
    transform: translateX(-50%);
    writing-mode: vertical-rl;
    font-size: 20px;
    line-height: 23px;
    font-weight: 800;
    color: #ffffff;
    white-space: nowrap;
  }
  .code-divider {
    position: absolute;
    left: 17px;
    width: 74px;
    height: 1px;
    background: #7a8696;
  }
  .seal-edge {
    position: absolute;
    left: -5px;
    width: 5px;
    background: linear-gradient(to bottom, rgba(40,163,228,0) 0%, var(--blue) 45%, var(--blue) 100%);
  }
</style>
</head>
<body>

  <!-- Version with sterile seal extension -->
  <section class="label label--seal">
    <div class="label-card" style="left:289px; top:189px; width:464px; height:353px;">
      <div class="card-mark" style="left:110px; top:40px; width:270px; height:270px;"></div>
      <div class="field" style="top:46px;">Name:<span class="field-rule"></span></div>
      <div class="field" style="top:93px;">Date of Birth:<span class="field-rule"></span></div>
      <div class="field" style="top:139px;">Date:<span class="field-rule"></span></div>
      <div class="field" style="top:186px;">Time:<span class="field-rule"></span></div>
      <div class="field" style="top:233px;">Temp:<span class="field-rule"></span></div>
      <div class="field" style="top:279px;">Specimen ID:<span class="field-rule"></span></div>
    </div>
    <div class="brand-strip" style="left:752px; top:111px; height:431px;">
      <div class="code-band"></div>
      <div class="brand-dot" style="top:27px;"></div>
      <div class="brand-name" style="top:82px;">Vela Drug Tests</div>
      <div class="product-code" style="top:340px;">TUB-47<br>90 mL</div>
    </div>
  </section>

  <!-- Version without sterile seal extension -->
  <section class="label label--plain">
    <div class="label-card" style="left:289px; top:706px; width:468px; height:356px;">
      <div class="card-mark" style="left:112px; top:40px; width:274px; height:274px;"></div>
      <div class="field" style="top:46px;">Name:<span class="field-rule"></span></div>
      <div class="field" style="top:93px;">Date of Birth:<span class="field-rule"></span></div>
      <div class="field" style="top:140px;">Date:<span class="field-rule"></span></div>
      <div class="field" style="top:187px;">Time:<span class="field-rule"></span></div>
      <div class="field" style="top:234px;">Temp:<span class="field-rule"></span></div>
      <div class="field" style="top:281px;">Specimen ID:<span class="field-rule"></span></div>
    </div>
    <div class="brand-strip" style="left:757px; top:626px; height:437px;">
      <div class="seal-edge" style="top:80px; bottom:0;"></div>
      <div class="brand-dot" style="top:28px;"></div>
      <div class="brand-name" style="top:82px;">Vela Drug Tests</div>
      <div class="code-divider" style="top:327px;"></div>
      <div class="product-code" style="top:346px;">TUB-47<br>90 mL</div>
    </div>
  </section>

</body>
</html>
```